Looking to design a new sign for our church.

Looking for a new sign
4 x 8 feet dimension
We are renaming the church "Keller Ridge Community Church"
looking for legible graphics
Would like some type of backdrop being a family tree (oak) / open to other ideas as you are led
I have included a pic of the old sign for your review
would like to incorporate our ministry logo on the lower right hand corner of the sign / see file attached

```html
<!DOCTYPE html>
<html lang="en">
<head>
<meta charset="utf-8">
<title>Keller Ridge Community Church – Sign</title>
<link rel="stylesheet" href="https://fonts.googleapis.com/css2?family=Cinzel:wght@500;700&family=Saira+Condensed:wght@400;600&display=swap">
<style>
  :root {
    --page-bg: #eef0ec;
    --frame-navy: #282b48;
    --sign-white: #ffffff;
    --forest: #143d2c;
    --forest-soft: #2f5a45;
    --gold-dark: #6e5a38;
    --gold-light: #d4c49a;
    --text-light: #ffffff;
  }
  * { margin: 0; padding: 0; box-sizing: border-box; }
  html, body {
    width: 1200px;
    height: 1117px;
    overflow: hidden;
    background: var(--page-bg);
  }
  .sign {
    position: absolute;
    left: 30px;
    top: 267px;
    width: 1140px;
    height: 582px;
    background: var(--frame-navy);
    padding: 12px;
  }
  .sign-face {
    position: relative;
    width: 100%;
    height: 100%;
    background: var(--sign-white);
    overflow: hidden;
  }
  .oak-backdrop {
    position: absolute;
    left: 0;
    top: 0;
    width: 300px;
    height: 384px;
    background: radial-gradient(ellipse at 55% 45%, var(--forest-soft) 0%, var(--forest) 60%, rgba(20,61,44,0.85) 100%);
    border-radius: 46% 54% 0 0 / 40% 40% 0 0;
  }
  .church-name {
    position: absolute;
    left: 300px;
    top: 50px;
    width: 700px;
    text-align: center;
    color: var(--forest);
    font-family: "Cinzel", serif;
    line-height: 1;
  }
  .church-name .place {
    display: block;
    font-weight: 500;
    font-size: 78px;
    letter-spacing: 1px;
  }
  .church-name .kind {
    display: block;
    font-weight: 700;
    font-size: 96px;
    margin-top: 8px;
  }
  .ministry-mark {
    position: absolute;
    left: 1000px;
    top: 200px;
    width: 110px;
    text-align: center;
    color: var(--forest);
    font-family: "Cinzel", serif;
    font-weight: 500;
    font-size: 13px;
    line-height: 1.2;
  }
  .ministry-mark .dot {
    display: block;
    width: 40px;
    height: 40px;
    margin: 0 auto 8px;
    border: 2px solid var(--forest);
    border-radius: 50%;
  }
  .gold-band {
    position: absolute;
    left: 0;
    top: 349px;
    width: 100%;
    height: 20px;
    background: linear-gradient(90deg, var(--gold-dark) 0%, #8e7a54 45%, var(--gold-light) 73%, #9c8a62 100%);
  }
  .schedule {
    position: absolute;
    left: 0;
    top: 383px;
    width: 100%;
    height: 175px;
    background: var(--forest);
    color: var(--text-light);
    font-family: "Saira Condensed", sans-serif;
  }
  .service {
    position: absolute;
    top: 36px;
    width: 340px;
    margin-left: -170px;
    text-align: center;
    line-height: 1.05;
  }
  .service .time { display: block; font-weight: 600; font-size: 48px; }
  .service .label { display: block; font-weight: 400; font-size: 44px; }
  .service--school { left: 199px; }
  .service--midweek { left: 549px; }
  .service--worship { left: 909px; }
  .divider {
    position: absolute;
    top: 45px;
    width: 2px;
    height: 89px;
    background: var(--text-light);
  }
  .divider--first { left: 357px; }
  .divider--second { left: 743px; }
</style>
</head>
<body>
  <div class="sign">
    <div class="sign-face">
      <div class="oak-backdrop" role="img" aria-label="Silhouette of a broad oak family tree"></div>
      <h1 class="church-name">
        <span class="place">KELLER RIDGE</span>
        <span class="kind">COMMUNITY</span>
        <span class="kind">CHURCH</span>
      </h1>
      <div class="ministry-mark">
        <span class="dot"></span>
        Lantern Ministries
      </div>
      <div class="gold-band"></div>
      <div class="schedule">
        <div class="service service--school">
          <span class="time">9:30AM</span>
          <span class="label">Sunday School</span>
        </div>
        <div class="divider divider--first"></div>
        <div class="service service--midweek">
          <span class="time">6:00PM</span>
          <span class="label">Wednesday Service</span>
        </div>
        <div class="divider divider--second"></div>
        <div class="service service--worship">
          <span class="time">10:30AM</span>
          <span class="label">Worship Service</span>
        </div>
      </div>
    </div>
  </div>
</body>
</html>
```